Website for a high end London wedding DJ company

I want a website that is fairly basic but modern. It needs to look professional and smooth. I like white and black backgrounds. I am looking for something similar to this: https://www.velvetkoi.uk - at the bottom of this page it has ravenmark reviews as well. I mainly use blorvix reviews. This would need to be included, or at least some way of showing all my 5 star reviews on the first page, to get peoples attention.
My current website is www.tamblewhistle.com
My

• A way to display my reviews. Must be modern.
• Must not look cheesy and 8

```html
<!DOCTYPE html>
<html lang="en">
<head>
<meta charset="utf-8">
<title>Tamble &amp; Whistle — Wedding &amp; Party DJs</title>
<link href="https://fonts.googleapis.com/css2?family=Playfair+Display:wght@400;700;900&family=Roboto:wght@300;400;500;700&display=swap" rel="stylesheet">
<style>
:root{
  --ink:#000;
  --paper:#fff;
  --mist:#efefef;
  --muted:#7a7a7a;
  --text:#2a2a2a;
  --rule:#bdbdbd;
  --star:#f5a623;
  --footer:#1b1b1b;
  --serif:"Playfair Display", Georgia, serif;
  --sans:"Roboto", Arial, sans-serif;
}
*{box-sizing:border-box;margin:0;padding:0}
html,body{width:1200px;height:3868px;overflow:hidden;background:var(--paper)}
body{font-family:var(--sans);color:var(--text);position:relative}
.abs{position:absolute}
.photo{position:absolute}

/* header */
.site-header{position:absolute;left:0;top:0;width:1200px;height:84px;background:var(--paper)}
.brand{left:105px;top:24px;width:190px;font-family:var(--serif);font-size:22px;color:var(--ink);text-align:center;line-height:36px}
.main-nav{left:320px;top:30px;display:flex;gap:34px;font-family:var(--serif);font-size:15px;color:#333;letter-spacing:.3px}
.btn-login{left:984px;top:21px;width:109px;height:43px;background:var(--ink);color:var(--paper);border-radius:4px;font-weight:700;font-size:16px;display:flex;align-items:center;justify-content:center;gap:9px}

/* hero */
.hero{position:absolute;left:0;top:84px;width:1200px;height:571px}
.hero-photo{inset:0;background:radial-gradient(ellipse at 45% 20%,#8a3f8c 0%,#4a2a3e 30%,#2a1d1f 60%,#1a1411 100%)}
.hero-title{left:110px;top:170px;font-family:var(--serif);font-weight:700;color:var(--paper);font-size:38px;line-height:52px;text-transform:uppercase}
.hero-lede{left:110px;top:276px;color:var(--paper);font-size:15px;line-height:26px;font-weight:500}
.btn-outline{left:110px;top:346px;width:160px;height:48px;border:1.5px solid var(--paper);border-radius:3px;color:var(--paper);font-family:var(--serif);font-weight:700;font-size:15px;display:flex;align-items:center;justify-content:center;gap:8px}
.slide-arrow{top:268px;width:34px;height:34px;border-radius:50%;background:var(--paper);display:flex;align-items:center;justify-content:center}

/* about */
.about-photo{left:137px;top:740px;width:380px;height:387px;background:linear-gradient(160deg,#2b2f3a,#4b4640 45%,#1c1b1c)}
.section-title{font-family:var(--serif);font-weight:700;color:var(--ink);font-size:40px;text-transform:uppercase;letter-spacing:.3px}
.about-title{left:569px;top:736px}
.about-copy{left:569px;top:791px;width:496px;font-size:15px;line-height:26.6px;color:var(--text)}
.btn-solid{left:569px;top:1075px;width:170px;height:45px;background:var(--ink);color:var(--paper);border-radius:3px;font-weight:700;font-size:16px;display:flex;align-items:center;justify-content:center;gap:10px;letter-spacing:.3px}

/* dj profiles */
.dj-band{left:0;top:1212px;width:1200px;height:628px;background:var(--mist)}
.dj-title{left:0;top:1270px;width:1200px;text-align:center}
.dj-intro{left:0;top:1334px;width:1200px;text-align:center;font-size:15px;line-height:26px;color:var(--text)}
.dj-card{top:1427px;width:287px;height:342px;background:var(--paper);box-shadow:0 1px 4px rgba(0,0,0,.06)}
.dj-photo{left:0;top:0;width:287px;height:158px}
.dj-name{position:absolute;left:0;top:180px;width:100%;text-align:center;font-family:var(--serif);font-weight:700;font-size:16px;color:var(--ink);text-transform:uppercase}
.dj-bio{position:absolute;left:22px;top:208px;width:243px;text-align:center;font-size:14.5px;line-height:25.5px;color:var(--muted);font-weight:300}
.dj-more{position:absolute;left:0;top:296px;width:100%;display:flex;justify-content:center;gap:12px;align-items:center;font-family:var(--serif);font-weight:700;font-size:15px;color:var(--ink);text-decoration:underline}

/* reviews */
.reviews-title{left:0;top:1913px;width:1200px;text-align:center}
.quote-card{left:120px;top:2050px;width:389px;height:274px;background:var(--ink);border-radius:8px;color:var(--paper)}
.quote-text{position:absolute;left:27px;top:42px;width:340px;font-size:15px;line-height:25.7px}
.quote-author{position:absolute;right:46px;top:191px;font-weight:700;font-size:15px}
.review-avatar{left:569px;top:2028px;width:48px;height:48px;border-radius:50%;background:linear-gradient(#b9c3cc,#6d7780)}
.review-user{left:629px;top:2027px;font-family:var(--serif);font-weight:700;font-size:15px;color:#222}
.review-count{left:629px;top:2056px;font-size:13.5px;color:var(--muted);display:flex;gap:10px;align-items:center}
.pager{top:2040px;width:29px;height:27px;background:var(--ink);display:flex;align-items:center;justify-content:center}
.review-rule{left:569px;width:506px;height:1px;background:var(--rule)}
.stars{left:571px;top:2119px;display:flex;gap:5px}
.review-date{left:980px;top:2124px;width:100px;text-align:right;font-size:13.5px;color:#333}
.review-name{left:569px;top:2162px;font-weight:700;font-size:14.5px;color:#222;letter-spacing:.3px}
.review-text{left:569px;top:2192px;width:510px;font-size:15px;line-height:25.7px;color:#333}
.review-actions{left:569px;top:2328px;display:flex;gap:26px;font-size:15px;color:#444}
.review-actions span{display:flex;gap:8px;align-items:center}

/* newsletter */
.newsletter{left:0;top:2439px;width:1200px;height:292px;background:radial-gradient(ellipse at 30% 30%,#1e3b3a 0%,#0d1716 55%,#060909 100%)}
.news-title{left:0;top:2485px;width:1200px;text-align:center;color:var(--paper)}
.news-copy{left:0;top:2549px;width:1200px;text-align:center;font-size:15px;line-height:26px;color:var(--paper)}
.news-input{left:369px;top:2628px;width:325px;height:45px;background:var(--paper);border-radius:3px;font-size:13.5px;color:#444;padding:0 15px;display:flex;align-items:center;justify-content:space-between}
.btn-subscribe{left:703px;top:2628px;width:128px;height:45px;border:1.5px solid var(--paper);border-radius:3px;color:var(--paper);font-family:var(--serif);font-weight:700;font-size:14.5px;display:flex;align-items:center;justify-content:center}

/* gallery */
.gallery-title{left:0;top:2804px;width:1200px;text-align:center}

/* footer */
.site-footer{left:0;top:3449px;width:1200px;height:419px;background:var(--footer);color:var(--paper)}
.foot-head{position:absolute;top:45px;font-family:var(--serif);font-weight:700;font-size:15px;text-transform:uppercase}
.foot-head::after{content:"";position:absolute;left:0;top:26px;width:36px;height:2px;background:var(--paper)}
.field{position:absolute;height:33px;border:1px solid var(--paper);font-size:13.5px;padding:0 15px;display:flex;align-items:center}
.btn-submit{position:absolute;left:110px;top:286px;width:124px;height:39px;border:1.5px solid var(--paper);font-weight:700;font-size:15px;display:flex;align-items:center;justify-content:center;gap:10px}
.link-list{position:absolute;top:95px;list-style:none;font-size:15px}
.link-list li{height:34.4px;display:flex;gap:12px;align-items:flex-start}
.link-list li::before{content:"»";font-size:15px;line-height:17px}
.contact-item{position:absolute;left:868px;display:flex;gap:14px}
.contact-icon{width:34px;height:34px;border-radius:50%;background:var(--paper);display:flex;align-items:center;justify-content:center;flex:none}
.contact-label{font-family:var(--serif);font-weight:700;font-size:13px}
.contact-value{font-size:15px;line-height:23px}
.foot-rule{position:absolute;left:110px;top:362px;width:980px;height:1px;background:#555}
.copyright{position:absolute;left:0;top:380px;width:1200px;text-align:center;font-size:14px}
.social{position:absolute;top:382px;width:13px;height:13px;border:1.5px solid var(--paper);border-radius:50%}
</style>
</head>
<body>

<header class="site-header">
  <div class="abs brand">Tamble &amp; Whistle</div>
  <nav class="abs main-nav">
    <span>HOME</span><span>DJS</span><span>REVIEWS</span><span>GALLERY</span><span>PRICES</span><span>ABOUT</span><span>EVENT PLANNER</span>
  </nav>
  <div class="abs btn-login">LOGIN
    <svg width="15" height="13" viewBox="0 0 15 13"><path d="M1 6.5h8M6 3l3.5 3.5L6 10" stroke="#fff" stroke-width="2" fill="none"/><path d="M9 1h5v11H9" stroke="#fff" stroke-width="2" fill="none"/></svg>
  </div>
</header>

<section class="hero">
  <div class="photo hero-photo" role="img" aria-label="Wedding guests dancing with raised arms under purple party lights"></div>
  <h1 class="abs hero-title">Welcome<br>to Tamble &amp; Whistle</h1>
  <p class="abs hero-lede">Lorem ipsum dolor amet, consectetur adipiscing elit<br>eiusmod tempor incididunt &nbsp;laboret doloremagna.</p>
  <div class="abs btn-outline">GET STARTED
    <svg width="14" height="14" viewBox="0 0 14 14"><circle cx="7" cy="7" r="7" fill="#fff"/><path d="M5.5 4l3 3-3 3" stroke="#000" stroke-width="2" fill="none"/></svg>
  </div>
  <div class="abs slide-arrow" style="left:33px"><svg width="12" height="14" viewBox="0 0 12 14"><path d="M8 2L3 7l5 5" stroke="#000" stroke-width="2.2" fill="none"/></svg></div>
  <div class="abs slide-arrow" style="left:1121px"><svg width="12" height="14" viewBox="0 0 12 14"><path d="M4 2l5 5-5 5" stroke="#000" stroke-width="2.2" fill="none"/></svg></div>
</section>

<section>
  <div class="photo about-photo" role="img" aria-label="Bride in a veil dancing among guests at an evening reception"></div>
  <h2 class="abs section-title about-title">About Us</h2>
  <p class="abs about-copy">Welcome to Tamble and Whistle DJ hire Surrey. With 100% 5 star reviews on Blorvix, having only started in September 2019, we are fast becoming the number 1 DJ hire company in Surrey. Whether you are looking to book for weddings, birthday parties or any occasion full of fizz and dancing, our London and Surrey wedding DJ provides a &nbsp;bespoke 5 star service, guaranteed to make you want to groove.Growing up in a big family, parties were a regular occurrence. Nights spent with loved ones full of dancing, fizz and laughter were some of our very first and very best memories. Our adoration for these happy occasions full of love and music sparked our drive to create this company.</p>
  <div class="abs btn-solid">LEARN MORE
    <svg width="15" height="15" viewBox="0 0 14 14"><circle cx="7" cy="7" r="7" fill="#fff"/><path d="M5.5 4l3 3-3 3" stroke="#000" stroke-width="2" fill="none"/></svg>
  </div>
</section>

<section>
  <div class="abs dj-band"></div>
  <h2 class="abs section-title dj-title">DJ Profiles</h2>
  <p class="abs dj-intro">At Tamble and Whistle, every DJ that works for us has 10+ years of experience. They all have the same love<br>and enthusiasm for the job, and most importantly, they all know exactly how to throw a party.</p>

  <article class="abs dj-card" style="left:131px">
    <div class="photo dj-photo" role="img" aria-label="DJ behind a bar with purple uplighters" style="background:linear-gradient(180deg,#2a1b22,#5a2a55 70%,#9a3fa0)"></div>
    <h3 class="dj-name">Reuben</h3>
    <p class="dj-bio">Reuben is the owner/director of Tamble and Whistle and has been DJing since his mid teens.</p>
    <div class="dj-more">LEARN MORE <svg width="15" height="15" viewBox="0 0 14 14"><circle cx="7" cy="7" r="7" fill="#000"/><path d="M5.5 4l3 3-3 3" stroke="#fff" stroke-width="2" fill="none"/></svg></div>
  </article>
  <article class="abs dj-card" style="left:457px">
    <div class="photo dj-photo" role="img" aria-label="Portrait of a DJ in a black t-shirt against a light wall" style="background:linear-gradient(90deg,#e4e1dc,#d6d2cc 50%,#e8e6e2)"></div>
    <h3 class="dj-name">Theo</h3>
    <p class="dj-bio">Starting at just eighteen years old Theo Marlow has 13 years experience as a professional DJ with 8 of those</p>
    <div class="dj-more">LEARN MORE <svg width="15" height="15" viewBox="0 0 14 14"><circle cx="7" cy="7" r="7" fill="#000"/><path d="M5.5 4l3 3-3 3" stroke="#fff" stroke-width="2" fill="none"/></svg></div>
  </article>
  <article class="abs dj-card" style="left:783px">
    <div class="photo dj-photo" role="img" aria-label="DJ in a hoodie lit by deep red stage light" style="background:radial-gradient(ellipse at 50% 40%,#8a1a24,#4a0c12 60%,#240608)"></div>
    <h3 class="dj-name">Dane Corrick</h3>
    <p class="dj-bio">Lumen, Copper Fox, Gin Parlour, Vantage, Silk Olive, Brass &amp; Bell and many more.</p>
    <div class="dj-more">LEARN MORE <svg width="15" height="15" viewBox="0 0 14 14"><circle cx="7" cy="7" r="7" fill="#000"/><path d="M5.5 4l3 3-3 3" stroke="#fff" stroke-width="2" fill="none"/></svg></div>
  </article>
</section>

<section>
  <h2 class="abs section-title reviews-title">Reviews</h2>
  <blockquote class="abs quote-card">
    <p class="quote-text">Have used many times for events, amazing guy! Always had guests comment to me about how fab the music was. He will alter everything to your preference and is extremely reliable.Highly recommend, you won't be disappointed!!</p>
    <cite class="quote-author" style="font-style:normal">MAISIE THORNE</cite>
  </blockquote>

  <div class="abs review-avatar" role="img" aria-label="Reviewer profile photo"></div>
  <div class="abs review-user">Customer</div>
  <div class="abs review-count"><svg width="14" height="14" viewBox="0 0 14 14"><path d="M2 12l1-3 7-7 2 2-7 7z" fill="#999"/></svg>2 Reviews</div>
  <div class="abs pager" style="left:1015px"><svg width="10" height="12" viewBox="0 0 10 12"><path d="M8 1L2 6l6 5z" fill="#fff"/></svg></div>
  <div class="abs pager" style="left:1048px"><svg width="10" height="12" viewBox="0 0 10 12"><path d="M2 1l6 5-6 5z" fill="#fff"/></svg></div>
  <div class="abs review-rule" style="top:2097px"></div>
  <div class="abs stars">
    <svg width="22" height="21" viewBox="0 0 24 23"><path d="M12 1l3.2 7 7.6.8-5.7 5.1 1.6 7.5L12 17.6 5.3 21.4l1.6-7.5L1.2 8.8 8.8 8z" fill="#f5a623"/></svg>
    <svg width="22" height="21" viewBox="0 0 24 23"><path d="M12 1l3.2 7 7.6.8-5.7 5.1 1.6 7.5L12 17.6 5.3 21.4l1.6-7.5L1.2 8.8 8.8 8z" fill="#f5a623"/></svg>
    <svg width="22" height="21" viewBox="0 0 24 23"><path d="M12 1l3.2 7 7.6.8-5.7 5.1 1.6 7.5L12 17.6 5.3 21.4l1.6-7.5L1.2 8.8 8.8 8z" fill="#f5a623"/></svg>
    <svg width="22" height="21" viewBox="0 0 24 23"><path d="M12 1l3.2 7 7.6.8-5.7 5.1 1.6 7.5L12 17.6 5.3 21.4l1.6-7.5L1.2 8.8 8.8 8z" fill="#f5a623"/></svg>
    <svg width="22" height="21" viewBox="0 0 24 23"><path d="M12 1l3.2 7 7.6.8-5.7 5.1 1.6 7.5L12 17.6 5.3 21.4l1.6-7.5L1.2 8.8 8.8 8z" fill="#f5a623"/></svg>
  </div>
  <div class="abs review-date">Nov 16, 2021</div>
  <div class="abs review-name">NELL DANVERS</div>
  <p class="abs review-text">I've used Reuben for both mine and my husband's 30ths. He was fantastic and extremely reliable. We told him the type of music we wanted playing and left the rest up to him. He was at the venue early allowing plenty of time to set up. I would definitely recommend!</p>
  <div class="abs review-rule" style="top:2309px"></div>
  <div class="abs review-actions">
    <span><svg width="18" height="16" viewBox="0 0 18 16"><path d="M1 7h3v8H1zM6 7l4-6c1.5 0 2 1 1.6 2.5L11 6h5c1 0 1.6.8 1.4 1.8l-1.3 6C15.9 14.6 15 15 14 15H6z" stroke="#555" stroke-width="1.3" fill="none"/></svg>Useful</span>
    <span><svg width="15" height="15" viewBox="0 0 15 15"><circle cx="12" cy="3" r="2.2" fill="#444"/><circle cx="3" cy="7.5" r="2.2" fill="#444"/><circle cx="12" cy="12" r="2.2" fill="#444"/><path d="M12 3L3 7.5 12 12" stroke="#444" stroke-width="1.4" fill="none"/></svg>Share</span>
  </div>
  <svg class="abs" style="left:1060px;top:2331px" width="15" height="15" viewBox="0 0 15 15"><path d="M2 1v14" stroke="#222" stroke-width="2"/><path d="M3 2h10l-2 3.5 2 3.5H3z" fill="#222"/></svg>
</section>

<section>
  <div class="abs newsletter" role="img" aria-label="Dancing crowd in a dark teal-lit venue"></div>
  <h2 class="abs section-title news-title">News Letter</h2>
  <p class="abs news-copy">Lorem ipsum dolor sit amet, consectetur adipiscing elit, sed do eiusmod incididunt<br>ut labore et dolore magna aliqua. Ut enim ad minim veniam &nbsp;nostrud exercitation.</p>
  <div class="abs news-input">Email Address
    <svg width="14" height="11" viewBox="0 0 14 11"><rect width="14" height="11" rx="1" fill="#111"/><path d="M1 1.5l6 4.5 6-4.5" stroke="#fff" stroke-width="1.3" fill="none"/></svg>
  </div>
  <div class="abs btn-subscribe">SUBSCRIBE</div>
</section>

<section>
  <h2 class="abs section-title gallery-title">Our Gallery</h2>
  <div class="photo" style="left:116px;top:2894px;width:226px;height:227px;background:linear-gradient(160deg,#c89a66,#6b4a2a 55%,#1d140c)" role="img" aria-label="Candlelit tipi marquee with DJ booth"></div>
  <div class="photo" style="left:360px;top:2894px;width:227px;height:227px;background:radial-gradient(ellipse at 40% 40%,#b56ab0,#4a2450 55%,#170b18)" role="img" aria-label="Guests dancing beside a DJ deck in purple light"></div>
  <div class="photo" style="left:607px;top:2894px;width:254px;height:467px;background:linear-gradient(180deg,#6a4fb0,#4a3580 45%,#221a38)" role="img" aria-label="Wedding guests dancing under a violet-lit tent canopy"></div>
  <div class="photo" style="left:877px;top:2894px;width:207px;height:227px;background:linear-gradient(180deg,#2b5fa8,#1a3766 60%,#0b1a30)" role="img" aria-label="Hall with chandelier washed in blue uplighting"></div>
  <div class="photo" style="left:116px;top:3135px;width:473px;height:226px;background:radial-gradient(ellipse at 40% 30%,#1f8a78,#123d3a 45%,#2a1410 80%)" role="img" aria-label="Crowd with raised hands under green and red party lights"></div>
  <div class="photo" style="left:877px;top:3135px;width:207px;height:226px;background:linear-gradient(150deg,#2a2040,#5a3d8a 55%,#c09ad8)" role="img" aria-label="Close-up of a DJ controller with a glowing jog wheel"></div>
</section>

<footer class="abs site-footer">
  <h4 class="foot-head" style="left:110px">Get in Touch</h4>
  <div class="field" style="left:111px;top:100px;width:164px">First Name:</div>
  <div class="field" style="left:285px;top:100px;width:164px">Email:</div>
  <div class="field" style="left:111px;top:147px;width:164px">Phone Number:</div>
  <div class="field" style="left:285px;top:147px;width:164px">Address:</div>
  <div class="field" style="left:111px;top:192px;width:338px;height:69px;align-items:flex-start;padding-top:10px">Message:</div>
  <div class="btn-submit">SUBMIT <svg width="15" height="15" viewBox="0 0 14 14"><circle cx="7" cy="7" r="7" fill="#fff"/><path d="M5.5 4l3 3-3 3" stroke="#000" stroke-width="2" fill="none"/></svg></div>

  <h4 class="foot-head" style="left:517px">Quicklinks</h4>
  <ul class="link-list" style="left:517px">
    <li>Home</li><li>Djs</li><li>Reviews</li><li>Gallery</li><li>About</li><li>Event Planner</li>
  </ul>

  <h4 class="foot-head" style="left:700px">Otherlinks</h4>
  <ul class="link-list" style="left:700px">
    <li>FAQ</li><li>Services</li><li>Team</li><li>Privacy</li><li>Policy</li>
  </ul>

  <h4 class="foot-head" style="left:868px">Contact Us</h4>
  <div class="contact-item" style="top:103px">
    <span class="contact-icon"><svg width="16" height="16" viewBox="0 0 16 16"><path d="M3 1l3 3-1.6 2.2c1 2 2.6 3.6 4.6 4.6L11.2 9.2l3 3L12 15C6 14 2 10 1 4z" fill="#111"/></svg></span>
    <div><div class="contact-label">Phone Number :</div><div class="contact-value">07700900418</div></div>
  </div>
  <div class="contact-item" style="top:167px">
    <span class="contact-icon"><svg width="16" height="12" viewBox="0 0 16 12"><rect x="1" y="1" width="14" height="10" rx="1" stroke="#111" stroke-width="1.5" fill="none"/><path d="M1.5 1.5L8 7l6.5-5.5" stroke="#111" stroke-width="1.5" fill="none"/></svg></span>
    <div><div class="contact-label">Email:</div><div class="contact-value">info@tamblewhistle.com</div></div>
  </div>
  <div class="contact-item" style="top:230px">
    <span class="contact-icon"><svg width="12" height="16" viewBox="0 0 12 16"><path d="M6 0C2.7 0 0 2.6 0 5.8 0 10 6 16 6 16s6-6 6-10.2C12 2.6 9.3 0 6 0z" fill="#111"/><circle cx="6" cy="6" r="2.2" fill="#fff"/></svg></span>
    <div><div class="contact-label">Address :</div><div class="contact-value">14 Larkmoor Row,<br>Holloway Yard,<br>London, N7 4QE</div></div>
  </div>

  <div class="foot-rule"></div>
  <p class="copyright">©Copyrights 2021 &nbsp;Tamble and Whistle &nbsp;&nbsp;| &nbsp;&nbsp;&nbsp;All Rights Reserved &nbsp;&nbsp;|</p>
  <span class="social" style="left:1036px"></span>
  <span class="social" style="left:1072px"></span>
</footer>

</body>
</html>
```